Guinea Pigs and Budgerigars Stud card design

The stud name for our animals is "Tarrinja" We offer a service for stud cavies (guinea pigs) and offer show and pet stock for sale. We also have show and pet stock for sale for show budgerigars as well

The animals/birds we show are very beautiful and we are a very professional stud. Our property entrance is in Black so we would also like to reflect that in the card, with Tarrinja and all writing in black. We can supply 2 photos to be integrated into the card, one of a black guinea pig and one of a yellow budgerigar. Tarrinja also means 'place of many owls' so we would also like an owl (not a cartoon type, a natural looking owl, preferably an australian barn owl) integrated into the design as well :)
Updates

Please also add the website address to the design
http://www.tarrinjafarm.example

Target Market(s)

professional animal breeders and families new to the industry

Industry/Entity Type

Pet

Contact Information for Business Card

Tarrinja
Joanne Petrakis and Malcolm Varga
Mallowbrook Flat Qld
0417 628 903

Requirements
Must have
• card to integrate 2 photos plus an owl ( I will try to find an example pic)

```html
<!DOCTYPE html>
<html lang="en">
<head>
<meta charset="utf-8">
<title>Tarrinja – Stud Business Card</title>
<link href="https://fonts.googleapis.com/css2?family=PT+Sans:wght@400&display=swap" rel="stylesheet">
<style>
  :root {
    --timber-light: #f1f1f1;
    --timber-mid: #d9d9d9;
    --panel-dark: #1f1f1f;
    --panel-mid: #5a5a5a;
    --ink: #111111;
    --pill: #0c0c0c;
    --pill-text: #ffffff;
    --owl-light: #e9e2d2;
    --owl-dark: #5a4330;
    --budgie-yellow: #e4ec3a;
    --budgie-green: #8cc63f;
    --cavy-grey: #7d7d7d;
    --font-main: "PT Sans", "Myriad Pro", Arial, sans-serif;
  }
  html, body {
    margin: 0;
    padding: 0;
    overflow: hidden;
    background: #ffffff;
  }
  .card {
    position: relative;
    width: 1200px;
    height: 693px;
    overflow: hidden;
    font-family: var(--font-main);
    background: linear-gradient(100deg, var(--timber-mid) 0%, var(--timber-light) 45%, #e4e4e4 100%);
  }
  .dark-panel {
    position: absolute;
    left: 0;
    top: 0;
    width: 395px;
    height: 693px;
    background: linear-gradient(90deg, var(--panel-dark) 0%, #3a3a3a 55%, var(--panel-mid) 100%);
  }
  .stud-name {
    position: absolute;
    left: 140px;
    top: 44px;
    margin: 0;
    font-size: 238px;
    font-weight: 400;
    line-height: 1;
    letter-spacing: -4px;
    background: linear-gradient(180deg, #f5f5f5 0%, #9a9a9a 40%, #2a2a2a 75%, #6b6b6b 100%);
    -webkit-background-clip: text;
    background-clip: text;
    color: transparent;
  }
  .photo {
    position: absolute;
  }
  .photo--owl {
    left: 34px;
    top: 378px;
    width: 305px;
    height: 315px;
    border-radius: 48% 48% 0 0;
    background: radial-gradient(ellipse at 50% 38%, var(--owl-light) 0%, #cfc3a8 45%, var(--owl-dark) 100%);
  }
  .photo--cavy-budgie {
    left: 873px;
    top: 203px;
    width: 327px;
    height: 283px;
    border-radius: 45% 10% 10% 40%;
    background: linear-gradient(90deg, var(--cavy-grey) 0%, #9a9a9a 30%, var(--budgie-green) 62%, var(--budgie-yellow) 100%);
  }
  .photo--bird-mark {
    left: 706px;
    top: 584px;
    width: 80px;
    height: 48px;
    border-radius: 50% 50% 40% 40%;
    background: linear-gradient(90deg, #3c3c3c, #6a6a6a);
  }
  .owners {
    position: absolute;
    left: 438px;
    top: 472px;
    width: 674px;
    height: 50px;
    border-radius: 10px;
    background: linear-gradient(180deg, #4a4a4a 0%, var(--pill) 55%);
    color: var(--pill-text);
    font-size: 33px;
    line-height: 50px;
    text-align: center;
    margin: 0;
  }
  .contact {
    position: absolute;
    left: 452px;
    top: 532px;
    margin: 0;
    color: var(--ink);
    font-size: 35px;
    line-height: 52px;
  }
  .contact span { display: block; }
</style>
</head>
<body>
  <div class="card">
    <div class="dark-panel"></div>

    <h1 class="stud-name">Tarrinja</h1>

    <div class="photo photo--owl" role="img" aria-label="Photograph of an Australian barn owl"></div>
    <div class="photo photo--cavy-budgie" role="img" aria-label="Photograph of a guinea pig beside a yellow and green budgerigar"></div>

    <p class="owners">Joanne Petrakis and Malcolm Varga</p>

    <p class="contact">
      <span class="contact__location">Mallowbrook Flat Qld</span>
      <span class="contact__phone">0417 628 903</span>
    </p>

    <div class="photo photo--bird-mark" role="img" aria-label="Small silhouette of a perched bird"></div>
  </div>
</body>
</html>
```